business card, stationary, email signature, envelopes
Bold Grins, PLLC
business card, stationary, email signature, envelopes - Medical
Creative Brief
Bright & Fun-filled
714 Harwick Ave Dover, NH 03827
boldgrinspllc@quorvamail.com
BoldGrinsPLLC.com

```html
<!DOCTYPE html>
<html lang="en">
<head>
<meta charset="utf-8">
<title>Bold Grins, PLLC — Stationery Set</title>
<link href="https://fonts.googleapis.com/css2?family=Nunito+Sans:wght@400;600;800&display=swap" rel="stylesheet">
<style>
:root{
  --bg:#eceef0;
  --paper:#ffffff;
  --navy:#1b2c9c;
  --blue:#2a7ce0;
  --sky:#7dc0f2;
  --pink:#e4167c;
  --ink:#4a4f5c;
  --shadow:0 2px 6px rgba(0,0,0,.18);
}
*{box-sizing:border-box;margin:0;padding:0}
html,body{width:1200px;height:936px;overflow:hidden}
body{background:var(--bg);font-family:"Nunito Sans",Arial,sans-serif;color:var(--ink);position:relative}
.sheet{position:absolute;background:var(--paper);box-shadow:var(--shadow);overflow:hidden}
.wave{position:absolute;left:0;bottom:0;width:100%}
.brand{font-weight:800;color:var(--navy);white-space:nowrap;display:flex;align-items:center;gap:.35em;letter-spacing:-.01em}
.brand .dot{width:.55em;height:.55em;border-radius:50%;background:var(--pink);display:inline-block}

/* Letterhead */
.letterhead{left:190px;top:20px;width:406px;height:698px}
.letterhead .brand{position:absolute;left:34px;top:34px;font-size:24px}
.letter-body{position:absolute;left:34px;top:112px;width:300px;font-size:6.5px;line-height:1.55}
.letter-body p{margin-bottom:9px}
.signature-line{width:50px;height:14px;border-bottom:1px solid var(--ink);margin:4px 0 3px}
.letter-contact{position:absolute;right:22px;bottom:32px;text-align:right;color:#fff;font-size:6.5px;line-height:1.8}
.letter-contact .gap{height:8px}

/* Folder */
.folder{left:634px;top:20px;width:533px;height:698px}
.folder .brand{position:absolute;left:50%;top:250px;transform:translateX(-50%);font-size:52px}
.folder .site{position:absolute;right:30px;bottom:28px;color:#fff;font-size:17px;letter-spacing:.08em}

/* Business cards */
.card{width:157px;height:84px;left:89px}
.card-front{top:730px}
.card-back{top:825px}
.card .brand{position:absolute;font-size:13px}
.card-front .brand{left:8px;top:10px}
.card-back .brand{left:10px;top:20px}
.card-details{position:absolute;right:6px;top:8px;text-align:right;font-size:4.2px;line-height:1.55}
.card-details .name{font-weight:800;color:var(--navy);font-size:5px}

/* Envelopes */
.envelope{top:736px;width:457px;height:182px}
.env-front{left:266px}
.env-front .brand{position:absolute;left:22px;top:20px;font-size:22px}
.env-front .return{position:absolute;left:22px;top:52px;font-size:7px}
.env-front .site{position:absolute;right:22px;bottom:14px;color:#fff;font-size:10px;letter-spacing:.08em}
.env-back{left:736px;background:var(--navy)}
.env-back .site{position:absolute;left:0;right:0;top:48px;text-align:center;color:#fff;font-size:11px;letter-spacing:.12em;z-index:2}
.env-back svg{position:absolute;left:0;top:0;width:100%;height:100%}
</style>
</head>
<body>

<!-- Letterhead -->
<section class="sheet letterhead">
  <div class="brand"><span>Bold Grins, PLLC</span><span class="dot"></span></div>
  <div class="letter-body">
    <p>July 8, 2024</p>
    <p>Dear Patient,<br>Care Team, Dover Office</p>
    <p>Thank you for choosing our practice for your family's dental care. We are glad to welcome you and look forward to helping every member of your household keep a healthy, bright smile for years to come.</p>
    <p>Our team offers gentle cleanings, whitening, fillings and orthodontic checks in a calm and friendly office. Please call us any time with questions about your visit or your treatment plan.</p>
    <p>We will send a reminder before each appointment. Thank you again for your trust.</p>
    <p>Best Regards,</p>
    <div class="signature-line"></div>
    <p>Dana Whitfield<br>Office Manager</p>
  </div>
  <svg class="wave" viewBox="0 0 400 210" preserveAspectRatio="none" height="210">
    <path d="M0 150 C120 90 250 60 400 40 L400 210 L0 210Z" fill="var(--navy)"/>
    <path d="M0 125 C130 70 260 45 400 18 L400 45 C250 62 120 95 0 155Z" fill="var(--blue)"/>
    <path d="M0 110 C140 55 270 30 400 5" stroke="var(--sky)" stroke-width="2" fill="none"/>
    <path d="M0 100 C150 50 280 25 400 0" stroke="var(--sky)" stroke-width="1" fill="none"/>
  </svg>
  <div class="letter-contact">
    714 Harwick Ave Dover,<br>NH 03827
    <div class="gap"></div>
    T (603) 555-0148<br>F (603) 555-0149<br>boldgrinspllc@quorvamail.com<br>BoldGrinsPLLC.com
  </div>
</section>

<!-- Presentation folder -->
<section class="sheet folder">
  <div class="brand"><span>Bold Grins, PLLC</span><span class="dot"></span></div>
  <svg class="wave" viewBox="0 0 400 200" preserveAspectRatio="none" height="200">
    <path d="M0 130 C120 70 260 50 400 35 L400 200 L0 200Z" fill="var(--navy)"/>
    <path d="M0 105 C130 50 270 30 400 12 L400 38 C260 55 120 80 0 135Z" fill="var(--blue)"/>
    <path d="M0 92 C140 40 280 20 400 0" stroke="var(--sky)" stroke-width="1.5" fill="none"/>
  </svg>
  <div class="site">BoldGrinsPLLC.com</div>
</section>

<!-- Business card front -->
<section class="sheet card card-front">
  <div class="brand"><span>Bold Grins, PLLC</span></div>
  <div class="card-details" style="top:30px">
    <div class="name">Dana Whitfield, DDS</div>
    Office Manager<br>T (603) 555-0148<br>boldgrinspllc@quorvamail.com
  </div>
  <svg class="wave" viewBox="0 0 400 80" preserveAspectRatio="none" height="22">
    <path d="M0 60 C140 20 270 10 400 0 L400 80 L0 80Z" fill="var(--navy)"/>
    <path d="M0 45 C140 10 270 0 400 -5" stroke="var(--sky)" stroke-width="4" fill="none"/>
  </svg>
</section>

<!-- Business card back -->
<section class="sheet card card-back">
  <div class="brand"><span>Bold Grins, PLLC</span><span class="dot"></span></div>
  <svg class="wave" viewBox="0 0 400 80" preserveAspectRatio="none" height="28">
    <path d="M0 55 C140 15 270 8 400 0 L400 80 L0 80Z" fill="var(--navy)"/>
    <path d="M0 40 C140 5 270 -2 400 -8" stroke="var(--blue)" stroke-width="6" fill="none"/>
  </svg>
</section>

<!-- Envelope front -->
<section class="sheet envelope env-front">
  <div class="brand"><span>Bold Grins, PLLC</span></div>
  <div class="return">714 Harwick Ave Dover, NH 03827</div>
  <svg class="wave" viewBox="0 0 400 90" preserveAspectRatio="none" height="70">
    <path d="M0 70 C140 30 270 15 400 5 L400 90 L0 90Z" fill="var(--navy)"/>
    <path d="M0 55 C140 18 270 5 400 -2 L400 10 C270 20 140 35 0 72Z" fill="var(--blue)"/>
    <path d="M0 48 C140 12 270 0 400 -6" stroke="var(--sky)" stroke-width="1.5" fill="none"/>
  </svg>
  <div class="site">BoldGrinsPLLC.com</div>
</section>

<!-- Envelope back -->
<section class="sheet envelope env-back">
  <svg viewBox="0 0 457 182" preserveAspectRatio="none">
    <path d="M0 0 L457 0 L457 34 L228 100 L0 34Z" fill="var(--paper)"/>
    <path d="M0 34 L228 100 L457 34" stroke="var(--blue)" stroke-width="2" fill="none"/>
  </svg>
  <div class="site" style="top:118px">BoldGrinsPLLC.com</div>
</section>

</body>
</html>
```